Medical Billing - Professional Marketing Flier

We are needing help designing a clean and professional looking easy to read marketing flier for a medical billing practice. The text needs to be large enough to print. We are looking for a 5.5 x 8.5 design that we can edit the text as needed. I have included our logo and what we initially want it to say. Please keep in mind, we also want our logo and contact details on the flier. Let me know if you have any questions.

```html
<!DOCTYPE html>
<html lang="en">
<head>
<meta charset="utf-8">
<title>Lumen Medical Billing – Flier</title>
<link href="https://fonts.googleapis.com/css2?family=Archivo+Black&family=Heebo:wght@300&family=Open+Sans:wght@400;600&family=Oswald:wght@600&family=Crimson+Text:ital@1&display=swap" rel="stylesheet">
<style>
  :root {
    --black: #000000;
    --blue-deep: #0a62b0;
    --blue-mid: #1a72c0;
    --blue-navy: #0b4a8a;
    --cyan: #0bb4e8;
    --footer-blue: #1a87c9;
    --text: #1a1a1a;
    --white: #ffffff;
    --logo-violet: #b57bd0;
  }
  * { margin: 0; padding: 0; box-sizing: border-box; }
  html, body { width: 887px; height: 1200px; overflow: hidden; background: var(--white); }
  .flier { position: relative; width: 887px; height: 1200px; overflow: hidden; font-family: "Open Sans", sans-serif; color: var(--text); }

  .hero { position: absolute; left: 0; top: 0; width: 887px; height: 438px; }
  .hero-photo {
    position: absolute; left: 380px; top: 0; width: 507px; height: 400px;
    background:
      radial-gradient(ellipse at 75% 25%, #6fa6d6 0%, #4f8cc4 35%, transparent 60%),
      linear-gradient(180deg, #3b3029 0%, #6b5a4c 30%, #d9dde2 60%, #eceef0 80%, #3a3d42 100%);
  }
  .hero-shapes { position: absolute; left: 0; top: 0; }

  .brand { position: absolute; left: 40px; top: 90px; width: 260px; text-align: center;
    font-family: "Open Sans", sans-serif; font-weight: 600; font-size: 23px; line-height: 32px; letter-spacing: 2px; color: var(--logo-violet); }

  .headline { position: absolute; left: 50px; top: 244px; width: 432px; color: var(--white); font-weight: normal; }
  .headline-lead { display: block; font-family: "Heebo", sans-serif; font-weight: 300; font-size: 29px; line-height: 36px; }
  .headline-line { display: block; font-family: "Archivo Black", sans-serif; font-size: 27px; line-height: 37px; text-align: justify; text-align-last: justify; }
  .headline-line.last { text-align-last: left; }

  .service { position: absolute; }
  .service-icon { position: absolute; left: 0; top: 0; width: 77px; height: 78px; }
  .service-title { position: absolute; font-family: "Archivo Black", sans-serif; font-weight: normal; font-size: 30px; line-height: 37px; color: var(--cyan); white-space: nowrap; }
  .service-text { position: absolute; left: 0; top: 104px; font-size: 14px; line-height: 17.6px; letter-spacing: 0.15px; text-align: justify; }

  .billing { left: 67px; top: 469px; }
  .aging { left: 497px; top: 469px; }
  .credentialing { left: 67px; top: 769px; }
  .contact { left: 497px; top: 769px; }
  .col-left .service-title { left: 101px; }
  .col-left .service-text { width: 358px; }
  .col-right .service-title { left: 95px; }
  .col-right .service-text { width: 331px; }

  .footer { position: absolute; left: 0; top: 1069px; width: 887px; height: 131px; background: var(--footer-blue); }
  .footer-pin { position: absolute; left: 44px; top: 41px; }
  .footer-address { position: absolute; left: 110px; top: 36px; font-family: "Oswald", sans-serif; font-weight: 600; font-size: 21px; line-height: 28px; color: var(--white); letter-spacing: -0.2px; }
  .footer-address .zip { margin-right: 8px; }
  .footer-email { position: absolute; left: 110px; top: 69px; font-family: "Crimson Text", serif; font-style: italic; font-size: 15px; line-height: 20px; color: var(--white); }
  .footer-bar { position: absolute; left: 416px; top: 47px; width: 471px; height: 41px; background: var(--black); border-radius: 6px 0 0 6px;
    display: flex; align-items: center; padding-left: 12px; color: var(--white); white-space: nowrap; }
  .footer-web { font-family: "Archivo Black", sans-serif; font-size: 17px; }
  .footer-divider { width: 1px; height: 24px; background: var(--white); margin: 0 8px; }
  .footer-phone { font-family: "Open Sans", sans-serif; font-size: 17px; }
</style>
</head>
<body>
<div class="flier">

  <header class="hero">
    <div class="hero-photo" role="img" aria-label="Photo of a clinician in blue scrubs using a tablet and a calculator at a desk with paperwork"></div>
    <svg class="hero-shapes" width="887" height="438" viewBox="0 0 887 438">
      <polygon points="0,184 323,184 362,80 592,438 0,438" fill="var(--blue-mid)"/>
      <polygon points="380,400 620,400 592,438 570,438" fill="var(--blue-mid)"/>
      <polygon points="0,184 120,184 270,438 0,438" fill="var(--blue-deep)"/>
      <polygon points="570,400 627,400 592,438" fill="var(--blue-navy)"/>
      <polygon points="390,0 462,0 400,110 362,80" fill="#e2e2e2"/>
      <polygon points="390,0 428,0 370,100 362,80" fill="var(--white)"/>
      <polygon points="0,0 390,0 323,184 0,184" fill="var(--black)"/>
    </svg>
    <div class="brand">LUMEN MEDICAL BILLING</div>
    <h1 class="headline">
      <span class="headline-lead">WE SPECIALIZE IN</span>
      <span class="headline-line">BILLING AND CONTRACTING</span>
      <span class="headline-line">FOR NUTRITIONISTS AND</span>
      <span class="headline-line last">DIETITIANS.</span>
    </h1>
  </header>

  <section class="service billing col-left">
    <svg class="service-icon" viewBox="0 0 57 64" preserveAspectRatio="none">
      <polygon points="28.5,0 57,16 57,48 28.5,64 0,48 0,16" fill="var(--cyan)"/>
      <rect x="24" y="13" width="16" height="30" fill="none" stroke="var(--white)" stroke-width="1.5"/>
      <rect x="20" y="16" width="16" height="30" fill="var(--cyan)" stroke="var(--white)" stroke-width="1.5"/>
      <rect x="14" y="19" width="18" height="30" fill="var(--white)"/>
      <g stroke="var(--cyan)" stroke-width="1.3">
        <line x1="17" y1="24" x2="29" y2="24"/><line x1="17" y1="28" x2="29" y2="28"/>
        <line x1="17" y1="32" x2="29" y2="32"/><line x1="17" y1="36" x2="29" y2="36"/>
        <line x1="17" y1="40" x2="29" y2="40"/><line x1="17" y1="44" x2="29" y2="44"/>
      </g>
    </svg>
    <h2 class="service-title" style="top:4px;">MEDICAL<br>BILLING</h2>
    <p class="service-text">Would you prefer to spend time focusing on your clients and running your practice rather than trying to stay up to speed with the constantly changing medical billing rules and regulations? Let us help you by managing your medical billing and dealing with the insurance companies on your behalf! We work with you to tailor the entire medical billing process to suit your practices needs while making it as smooth and painless as possible.</p>
  </section>

  <section class="service aging col-right">
    <svg class="service-icon" viewBox="0 0 57 64" preserveAspectRatio="none">
      <polygon points="28.5,0 57,16 57,48 28.5,64 0,48 0,16" fill="var(--cyan)"/>
      <circle cx="28.5" cy="32" r="19" fill="none" stroke="var(--white)" stroke-width="3" stroke-dasharray="3 3"/>
      <path d="M28.5 13 A19 19 0 0 1 47.5 32 A19 19 0 0 1 28.5 51 A19 19 0 0 1 13 42" fill="none" stroke="var(--white)" stroke-width="3"/>
      <polyline points="28.5,20 28.5,32 36,40" fill="none" stroke="var(--white)" stroke-width="2.5" stroke-linecap="round"/>
    </svg>
    <h2 class="service-title" style="top:21px;">AGING</h2>
    <p class="service-text">Are you leaving money on the table? Are you able to do the follow-through needed to keep your aging in check and more money flowing into your practice? Are you uncertain about how to get insurance to pay on claims that should be covered but for some reason they decided not to? We can clean up your aging, reduce the amount of time it takes for claims to pay out, and we can keep your aging to a minimum.</p>
  </section>

  <section class="service credentialing col-left">
    <svg class="service-icon" viewBox="0 0 57 64" preserveAspectRatio="none">
      <polygon points="28.5,0 57,16 57,48 28.5,64 0,48 0,16" fill="var(--cyan)"/>
      <rect x="14" y="12" width="29" height="40" fill="none" stroke="var(--white)" stroke-width="1.8"/>
      <g stroke="var(--white)" stroke-width="1.3">
        <line x1="18" y1="17" x2="39" y2="17"/><line x1="18" y1="21" x2="39" y2="21"/>
        <line x1="18" y1="25" x2="39" y2="25"/><line x1="18" y1="29" x2="39" y2="29"/>
        <line x1="18" y1="33" x2="39" y2="33"/><line x1="18" y1="40" x2="30" y2="40"/>
        <line x1="18" y1="46" x2="22" y2="46"/><line x1="25" y1="46" x2="30" y2="46"/>
      </g>
      <circle cx="36" cy="44" r="3" fill="none" stroke="var(--white)" stroke-width="1.5"/>
    </svg>
    <h2 class="service-title" style="top:21px;">CREDENTIALING</h2>
    <p class="service-text">Are you wanting to get contracted with insurance companies but aren’t sure how to go about it? Are you wanting to expand your client base by having the option to bill insurance? Let us take the confusion out of what can seem like a daunting task! We can get you and your practitioners contracted with the insurance companies of your choice and help you navigate through the process every step of the way!</p>
  </section>

  <section class="service contact col-right">
    <svg class="service-icon" viewBox="0 0 57 64" preserveAspectRatio="none">
      <polygon points="28.5,0 57,16 57,48 28.5,64 0,48 0,16" fill="var(--cyan)"/>
      <path d="M17 16 l6 -2 l5 9 l-4 4 c2 5 6 9 11 11 l4 -4 l9 5 l-2 6 c-2 3 -6 4 -10 2 c-9 -4 -16 -11 -20 -20 c-2 -4 -1 -8 1 -11 z" fill="none" stroke="var(--white)" stroke-width="2.2" stroke-linejoin="round"/>
    </svg>
    <h2 class="service-title" style="top:21px;">CONTACT US</h2>
    <p class="service-text">If any of these processes are something you would like our help with or to consult with us on, please email us or give us a call! We specialize in billing and contracting for Nutritionists and Dietitians. We would love to help you expand your business and take the pain and frustration out of billing so you can focus on your clients.</p>
  </section>

  <footer class="footer">
    <svg class="footer-pin" width="50" height="50" viewBox="0 0 50 50">
      <circle cx="25" cy="25" r="25" fill="var(--white)"/>
      <path d="M25 12 a9 9 0 0 1 9 9 c0 7 -9 17 -9 17 s-9 -10 -9 -17 a9 9 0 0 1 9 -9 z" fill="none" stroke="var(--footer-blue)" stroke-width="1.8"/>
      <circle cx="25" cy="21" r="3.5" fill="none" stroke="var(--footer-blue)" stroke-width="1.8"/>
    </svg>
    <div class="footer-address"><span class="zip">123457</span>Lorem ipsum dolor sit amet</div>
    <div class="footer-email">Online Support 123456789@example.com</div>
    <div class="footer-bar">
      <span class="footer-web">www.your website.com</span>
      <span class="footer-divider"></span>
      <span class="footer-phone">+123 456 78900</span>
    </div>
  </footer>

</div>
</body>
</html>
```